依頼詳細
現状はデザインの入ったアルミパックとなっておりますが、今回デザインした箱に無地のアルミパックを入れる方向に転換したいと思っておりますので、箱のデザインを依頼したいと思います。しかしながら、アルミパックのままデザインのみ変更する場合も考えられますので、どちらでも使えるデザインだと大変助かります。
記載項目
現状サイズ:たて約23cm×よこ約17cmのパック。
希望イメージ
シンプル 複雑
単色 カラフル
暗い 明るい
日常 高級
遊び心 厳粛
未来的 伝統的
女性的 男性的
希望する色
納品ファイル
• 高解像度JPG (.jpg)
• イラストレーター形式 (.ai)
補足説明
添付は現在の商品デザインになります。
皆様ご提案頂き誠にありがとうございます。
延長の理由を追記させて頂きます。
当方のイメージとしましては、全体的にもう少し「アート感」が欲しいところであります。
香川県はうどんだけでなく、直島などのアートの県としての特徴もございますので、その辺りを含んだデザインでお願い致します。
■ 選んだ理由

皆様たくさんのご提案誠にありがとうございました。
とても良いデザインが多いなか選考に時間がかかりましたが、個人的にパッと見たときのデザイン性、斬新さなどからこちらのデザインに決定させて頂きました。和をイメージして頂いたデザインも多かったですが、よくある和なイメージかなと思いましたのと、四国をイメージして頂いていたものも海外の方には分かりにくいかなと思い、今回のちょっと違った捉え方をした「和」とデザイン性(アート)の感じられたこちらのデザインに決定させて頂きました。皆様ご提案ありがとうございました。

■ 提案者全員のお礼・コメント

改めましてこの度は素晴らしいデザインのご提案、誠にありがとうございました。また早速コメントも返信頂きありがとうございます。後ほど一部修正案等まとめまして、ご相談させて頂きます。引き続きどうぞよろしくお願い致します。

```html
<!DOCTYPE html>
<html lang="ja">
<head>
<meta charset="utf-8">
<title>潮の音 天然だしパック</title>
<link rel="stylesheet" href="https://fonts.googleapis.com/css2?family=Shippori+Mincho:wght@500;700;800&family=Cormorant+Garamond:ital@0;1&display=swap">
<style>
:root{
  --paper:#ffffff;
  --kraft:#c59c5d;
  --orange:#e8591f;
  --orange-soft:#f07a3e;
  --ink:#2a1f1b;
  --white:#ffffff;
}
*{margin:0;padding:0;box-sizing:border-box}
html,body{width:857px;height:1200px;overflow:hidden;background:var(--paper)}
body{position:relative;font-family:"Shippori Mincho",serif;color:var(--ink)}
.sheet-code{position:absolute;left:22px;top:34px;font-family:"Cormorant Garamond",serif;font-size:38px;letter-spacing:1px;color:var(--ink)}
.package{position:absolute;left:80px;top:109px;width:698px;height:1011px;background:var(--kraft);overflow:hidden}
.pattern-disc{position:absolute;left:-170px;top:-25px;width:740px;height:740px;border-radius:50%;
  background:radial-gradient(circle at 40% 35%,var(--orange-soft),var(--orange) 70%)}
.headline{position:absolute;right:8px;top:34px;writing-mode:vertical-rl;font-size:34px;font-weight:800;letter-spacing:6px;line-height:1;color:var(--ink)}
.lead{position:absolute;right:62px;top:78px;writing-mode:vertical-rl;font-size:19px;font-weight:700;letter-spacing:4px;line-height:1.6;color:var(--ink)}
.brand-box{position:absolute;left:191px;top:277px;width:200px;height:200px;background:var(--ink);color:var(--white)}
.brand-name{position:absolute;left:0;right:0;top:50%;transform:translateY(-50%);text-align:center;font-size:34px;font-weight:500;letter-spacing:8px;padding-left:14px}
.brand-roman{position:absolute;left:12px;top:18px;writing-mode:vertical-rl;font-family:"Cormorant Garamond",serif;font-style:italic;font-size:11px;letter-spacing:3px;white-space:nowrap;opacity:.85}
.origin-badge{position:absolute;left:506px;top:786px;width:182px;height:182px;border-radius:50%;background:var(--orange);color:var(--white);font-weight:800}
.origin-badge .char{position:absolute;font-size:40px;line-height:1}
.origin-badge .c1{left:48px;top:34px}
.origin-badge .c2{left:94px;top:34px}
.origin-badge .c3{left:48px;top:82px}
.origin-badge .c4{left:94px;top:82px}
.origin-badge .use{position:absolute;left:0;right:0;top:132px;text-align:center;font-size:15px;letter-spacing:3px}
.contents{position:absolute;left:57px;top:884px;font-size:23px;font-weight:700;letter-spacing:1px;color:var(--ink)}
.swatches{position:absolute;left:508px;top:1158px;display:flex;gap:22px}
.swatch{width:52px;height:22px;border:1.5px solid var(--ink)}
.swatch.white{background:var(--white)}
.swatch.kraft{background:var(--kraft);border-color:var(--kraft)}
.swatch.orange{background:var(--orange);border-color:var(--orange)}
.swatch.ink{background:var(--ink)}
</style>
</head>
<body>
<div class="sheet-code">0723-A</div>
<main class="package">
  <div class="pattern-disc" role="img" aria-label="青海波と紗綾形の和柄を敷き詰めたオレンジの大きな円"></div>
  <h1 class="headline">天然だしパック</h1>
  <p class="lead">料亭の味をご家庭に<br>お届けします。</p>
  <div class="brand-box">
    <span class="brand-roman">shio no ne</span>
    <span class="brand-name">潮の音</span>
  </div>
  <div class="origin-badge">
    <span class="char c1">素</span>
    <span class="char c2">国</span>
    <span class="char c3">材</span>
    <span class="char c4">産</span>
    <span class="use">使用</span>
  </div>
  <p class="contents">個包装 20袋入（1袋4人分）</p>
</main>
<div class="swatches">
  <span class="swatch white"></span>
  <span class="swatch kraft"></span>
  <span class="swatch orange"></span>
  <span class="swatch ink"></span>
</div>
</body>
</html>
```